Specialized Personal Trainer Needs a Business Card Design

I need a business card design for my personal training business called Tall Oak Fitness. I have my Human Kinetics degree in Exercise Science from the Halvern Ridge University as well as an extra certification from NBEP (National Board of Exercise Practice). I work as a Cardiac Rehab Exercise Specialist and personal trainer giving specialized exercise prescriptions to those that have different heart conditions as well as work with the general population in weight loss, strength and conditioning, getting/staying fit.
Updates

I decided that I wanted a logo (as I did not have one before I submitted my project for a business card) so I am submitting a project to get a logo done and then I will decide on a business card, hopefully being able to use one of the designs already submitted.  My apologies for doing this backwards.  I am new to this so I appreciate your patience.

Thank you.

Hi, I have just created a project for a logo design (I realized I needed a logo and I should've done that first..oops!), please feel free to participate.  Once I receive a logo I like I will finalize my business card project and hopefully incorporate it into one of your business card designs. 

Thank you!

Target Market(s)

Business professionals

Industry/Entity Type

Personal Trainer

Requirements
Must have
• My name with my info:
Celia R. Dunhill (BHK)
NBEP Certified Clinical Exercise Specialist & Personal Trainer
celia.dunhill@talloakfitness.example
Cell: 604-358-4170

Please make it double sided.
Nice to have
• An image that represents cardiac and general fitness training.

```html
<!DOCTYPE html>
<html lang="en">
<head>
<meta charset="utf-8">
<title>Tall Oak Fitness – Business Card</title>
<link rel="stylesheet" href="https://fonts.googleapis.com/css2?family=Barlow:wght@400&family=Roboto+Condensed:wght@400;700;800&display=swap">
<style>
  :root {
    --brand-red: #e31b3a;
    --card-white: #ffffff;
    --page-bg: #ffffff;
    --card-edge: #d6d6d6;
    --card-shadow: rgba(0, 0, 0, 0.28);
  }
  * { margin: 0; padding: 0; box-sizing: border-box; }
  html, body {
    width: 1200px;
    height: 901px;
    overflow: hidden;
    background: var(--page-bg);
  }
  .canvas {
    position: relative;
    width: 1200px;
    height: 901px;
  }
  .card {
    position: absolute;
    left: 275px;
    width: 700px;
    height: 400px;
    border-radius: 32px;
    overflow: hidden;
    box-shadow: 0 6px 12px var(--card-shadow);
  }
  .card-front {
    top: 53px;
    background: var(--brand-red);
    display: flex;
    align-items: center;
    justify-content: center;
  }
  .wordmark {
    font-family: "Roboto Condensed", sans-serif;
    font-weight: 800;
    color: var(--card-white);
    text-align: center;
    text-transform: uppercase;
    line-height: 0.95;
    letter-spacing: -1px;
  }
  .wordmark-line-top { display: block; font-size: 92px; }
  .wordmark-line-bottom { display: block; font-size: 66px; }

  .card-back {
    top: 493px;
    background: var(--card-white);
    border: 1px solid var(--card-edge);
    color: var(--brand-red);
  }
  .services {
    position: absolute;
    left: 40px;
    top: 58px;
    font-family: "Barlow", sans-serif;
    font-size: 19px;
    letter-spacing: 1.6px;
    text-transform: uppercase;
    white-space: nowrap;
  }
  .services .divider { margin: 0 16px; }
  .contact {
    position: absolute;
    left: 40px;
    top: 143px;
    font-family: "Roboto Condensed", sans-serif;
  }
  .business-name {
    font-size: 31px;
    font-weight: 700;
    letter-spacing: -0.3px;
  }
  .person-name {
    margin-top: 18px;
    font-size: 27px;
    font-weight: 700;
    line-height: 1.1;
  }
  .person-name .credential { font-weight: 400; font-size: 25px; }
  .person-title {
    font-size: 19px;
    line-height: 1.2;
  }
  .contact-lines {
    margin-top: 26px;
    list-style: none;
    font-size: 23px;
    line-height: 30px;
  }
</style>
</head>
<body>
<main class="canvas">
  <section class="card card-front" aria-label="Card front">
    <h1 class="wordmark">
      <span class="wordmark-line-top">Tall Oak</span>
      <span class="wordmark-line-bottom">Fitness</span>
    </h1>
  </section>

  <section class="card card-back" aria-label="Card back">
    <p class="services">Training<span class="divider">|</span>Cardiac Rehabilitation<span class="divider">|</span>Wellness</p>
    <div class="contact">
      <h2 class="business-name">Tall Oak Fitness</h2>
      <p class="person-name">Celia R. Dunhill <span class="credential">(BHK)</span></p>
      <p class="person-title">NBEP Cert. &amp; Personal Trainer</p>
      <ul class="contact-lines">
        <li class="phone">604-358-4170</li>
        <li class="website">www.talloakfitness.example</li>
        <li class="email">celia.dunhill@talloakfitness.example</li>
      </ul>
    </div>
  </section>
</main>
</body>
</html>
```